Velvet Harbor Gentlemen's Club 20 YR Anniversary

Need artwork for:
9.65 inches (wide) x 5.34 inches (high) [newspaper ad]
Facebook Cover Photo
Facebook Profile Picture
The design should be consistent throughout the different sizes.

The document attached has the party information.

The party is for our 20 yr anniversary but the highlight of the event is FREE LAP DANCES FOR EVERYBODY
We'd like to use the colors black, red and gold but we are open to any artists thoughts and ideas.

I tried to attach a photo of the guest performer. But when I tried to upload it I received this message: Sorry, you can only upload files up to 4096px in width. At 5616px the file 'IMG_6454edit.jpg' is too wide. I've attached an alternate photo. I hope we can one of them.

Colors
fbed22
ec1f27

Requirements
Must have
• VHG logo
• FREE LAP DANCES FOR EVERYBODY
• No Gimmicks, No Catch...No Strings Attached

```html
<!DOCTYPE html>
<html lang="en">
<head>
<meta charset="utf-8">
<title>Velvet Harbor Gentlemen's Club – 20 Year Anniversary</title>
<link rel="stylesheet" href="https://fonts.googleapis.com/css2?family=Anton&family=Arimo:wght@400;700&family=Montserrat:wght@600&family=Parisienne&family=Oswald:wght@500;700&display=swap">
<style>
  :root {
    --paper: #ffffff;
    --panel: #000000;
    --frame-top: #e8134f;
    --frame-bottom: #6a1c7e;
    --gold: #d9b25c;
    --gold-light: #f0d68a;
    --gold-deep: #a77a2c;
    --magenta: #b1237f;
    --red: #e0185a;
    --white: #ffffff;
    --chair: #6b2c72;
    --chair-dark: #2a1030;
  }
  * { margin: 0; padding: 0; box-sizing: border-box; }
  html, body { width: 1200px; height: 745px; overflow: hidden; background: var(--paper); }
  .ad { position: relative; width: 1200px; height: 745px; }
  .ad__frame, .performer { position: absolute; left: 0; top: 0; }

  .anniversary { position: absolute; left: 213px; top: 170px; display: flex; align-items: center; }
  .anniversary__number {
    font-family: "Oswald", sans-serif; font-weight: 700; font-size: 60px; line-height: 1;
    background: linear-gradient(180deg, var(--gold-light), var(--gold-deep));
    -webkit-background-clip: text; background-clip: text; color: transparent;
    padding-right: 6px; border-right: 2px solid var(--gold);
  }
  .anniversary__label { padding-left: 6px; font-family: "Oswald", sans-serif; color: var(--gold); line-height: 1; }
  .anniversary__year { display: block; font-size: 36px; font-weight: 500; letter-spacing: 2px; border-bottom: 2px solid var(--gold); padding-bottom: 2px; }
  .anniversary__word { display: block; font-size: 14px; font-weight: 700; letter-spacing: 0.5px; padding-top: 3px; }

  .club-name {
    position: absolute; left: 482px; top: 162px;
    font-family: "Montserrat", sans-serif; font-weight: 600; font-size: 118px;
    color: var(--white); letter-spacing: -4px; line-height: 1;
  }

  .headline { position: absolute; left: 213px; top: 234px; }
  .headline__line {
    display: block; font-family: "Anton", sans-serif; font-size: 80px; line-height: 0.86;
    letter-spacing: 6px; text-transform: uppercase; transform: scaleX(1.12); transform-origin: left center;
    background: radial-gradient(circle, var(--gold-light) 1.5px, var(--gold-deep) 2px, transparent 2.4px) 0 0 / 6px 6px;
    -webkit-background-clip: text; background-clip: text; color: transparent;
  }
  .headline__script {
    position: absolute; left: -30px; top: 112px; white-space: nowrap;
    font-family: "Parisienne", cursive; font-weight: 400; font-size: 50px; color: var(--gold); letter-spacing: 8px;
  }

  .promise { position: absolute; left: 215px; top: 430px; font-family: "Arimo", sans-serif; font-weight: 700; font-size: 15px; letter-spacing: 3px; font-variant: small-caps; line-height: 22px; }
  .promise__first { color: var(--magenta); display: block; }
  .promise__second { color: var(--red); display: block; }

  .details { position: absolute; left: 215px; top: 471px; font-family: "Arimo", sans-serif; font-size: 15.5px; line-height: 19px; color: var(--white); }
  .details strong { font-weight: 700; }

  .web { position: absolute; left: 215px; top: 568px; font-family: "Arimo", sans-serif; font-weight: 700; font-size: 20px; color: var(--gold); letter-spacing: 0.5px; }
</style>
</head>
<body>
<main class="ad">
  <svg class="ad__frame" width="1200" height="745" viewBox="0 0 1200 745" aria-hidden="true">
    <defs>
      <linearGradient id="frameGradient" x1="0" y1="0" x2="0" y2="1">
        <stop offset="0" stop-color="#e8134f"/>
        <stop offset="1" stop-color="#6a1c7e"/>
      </linearGradient>
    </defs>
    <rect x="117" y="108" width="966" height="528" fill="url(#frameGradient)"/>
    <path fill="#ffffff" d="M149 122 H1051 A18 18 0 0 0 1069 140 V604 A18 18 0 0 0 1051 622 H149 A18 18 0 0 0 131 604 V140 A18 18 0 0 0 149 122 Z"/>
    <path fill="#000000" d="M164 139 H1036 A17 17 0 0 0 1053 156 V588 A17 17 0 0 0 1036 605 H164 A17 17 0 0 0 147 588 V156 A17 17 0 0 0 164 139 Z"/>
  </svg>

  <svg class="performer" width="1200" height="745" viewBox="0 0 1200 745" role="img" aria-label="Photograph of the guest performer reclining across a purple tufted armchair">
    <defs>
      <radialGradient id="performerTone" cx="0.62" cy="0.5" r="0.6">
        <stop offset="0" stop-color="#6b2c72"/>
        <stop offset="0.6" stop-color="#4a1d52"/>
        <stop offset="1" stop-color="#000000" stop-opacity="0"/>
      </radialGradient>
    </defs>
    <rect x="540" y="262" width="510" height="340" rx="28" fill="url(#performerTone)"/>
  </svg>

  <div class="anniversary">
    <span class="anniversary__number">20</span>
    <span class="anniversary__label">
      <span class="anniversary__year">YEAR</span>
      <span class="anniversary__word">ANNIVERSARY</span>
    </span>
  </div>

  <div class="club-name">VHG</div>

  <h1 class="headline">
    <span class="headline__line">Free</span>
    <span class="headline__line">Lapdances</span>
    <span class="headline__script">for everyone</span>
  </h1>

  <p class="promise">
    <span class="promise__first">No Gimmicks...No Catch...</span>
    <span class="promise__second">No Strings Attached!</span>
  </p>

  <p class="details">
    Catered Dinner by <strong>Bellavista Kitchen</strong> until 10pm<br>
    <strong>$3.50</strong> drinks all night | Featuring 3 Shows with<br>
    2015 Miss Nude Wisconsin, Scarlett Vane<br>
    Thursday May 12, 2016&nbsp; From 6pm until…<br>
    4820 Harbor Point Rd.&nbsp; Lakeview, WI 555-014-2277
  </p>

  <p class="web">www.vhg.clubfb/clubvhgwi</p>
</main>
</body>
</html>
```